Sandwich Board-

We need a (3) 24" X 36" PORTRAIT & 8.5 x11" Graphic Panels with a beautiful nature photo, waterfall or some nice photo with river, ponds or lake as background image.

BE SURE TO USE PHOTOS FROM TROPICAL ENVIRONMENTS - NOT WINTER ALPS ETC

Designer to find & select (2) photos to be used. (1) photo for each poster

I will pay for photos if required from photo licensing site

Poster is an Invitation to attend: "Velvet Ember Music Event" ( see attached photo)

Details of Event: see attached photo ( LEAVE OUT ADDRESS)

I PROVIDED A REAL ROUGH DRAFT AS A SAMPLE

Requirements
Must have
• The following text must be on each design
• 1. 412 Maneola rd. Pahoa
• 2. No Charge or Free Event
• 3. Every Sunday
• 4. Ph: 808.555.0193

```html
<!DOCTYPE html>
<html lang="en">
<head>
<meta charset="UTF-8">
<title>Velvet Ember Music Event – Poster</title>
<link rel="stylesheet" href="https://fonts.googleapis.com/css2?family=Kaushan+Script&family=Lobster&family=Montserrat:ital,wght@0,600;0,700;0,800;1,800&display=swap">
<style>
  :root {
    --navy: #1b2a6b;
    --royal: #1f4aa6;
    --red: #d9262b;
    --white: #ffffff;
    --scene-top: #7cc6e6;
    --scene-mid: #5aa77a;
    --scene-low: #8fdde0;
    --band: #1c2c6e;
  }
  * { margin: 0; padding: 0; box-sizing: border-box; }
  html, body { width: 800px; height: 1200px; overflow: hidden; background: #fff; }
  .poster {
    position: relative;
    width: 800px;
    height: 1200px;
    overflow: hidden;
    font-family: "Montserrat", Arial, sans-serif;
    color: var(--navy);
    text-align: center;
  }
  .scenery {
    position: absolute;
    inset: 0;
    background: linear-gradient(180deg, var(--scene-top) 0%, var(--scene-mid) 45%, var(--scene-low) 70%, #eaf8f8 100%);
  }
  .notes-art {
    position: absolute;
    top: 400px;
    left: 90px;
    width: 620px;
    height: 180px;
    border-radius: 90px;
    background: rgba(255,255,255,0.35);
  }
  .tagline {
    position: absolute;
    top: 160px;
    left: 0; right: 0;
    font-family: "Kaushan Script", cursive;
    font-size: 66px;
    font-weight: 400;
    line-height: 1.15;
    color: var(--navy);
    text-shadow: 0 0 10px rgba(255,255,255,0.85);
  }
  .event-name {
    position: absolute;
    top: 580px;
    left: 0; right: 0;
    font-family: "Lobster", cursive;
    font-size: 124px;
    font-weight: 400;
    line-height: 0.9;
    color: var(--royal);
    text-shadow:
      3px 3px 0 var(--white), -3px -3px 0 var(--white),
      3px -3px 0 var(--white), -3px 3px 0 var(--white),
      0 3px 0 var(--white), 0 -3px 0 var(--white),
      3px 0 0 var(--white), -3px 0 0 var(--white);
  }
  .event-type {
    position: absolute;
    top: 832px;
    left: 0; right: 0;
    font-size: 42px;
    font-weight: 800;
    letter-spacing: 14px;
    padding-left: 14px;
  }
  .admission {
    position: absolute;
    top: 886px;
    left: 0; right: 0;
    font-size: 28px;
    font-weight: 800;
    letter-spacing: 2px;
    color: var(--red);
  }
  .invitation {
    position: absolute;
    top: 926px;
    left: 0; right: 0;
    font-size: 25px;
    font-weight: 800;
    font-style: italic;
    line-height: 1.25;
  }
  .schedule {
    position: absolute;
    top: 1030px;
    left: 0; right: 0;
    font-size: 36px;
    font-weight: 800;
    font-style: italic;
    display: flex;
    justify-content: center;
    align-items: center;
    gap: 10px;
  }
  .schedule .time { color: var(--red); }
  .schedule svg { width: 32px; height: 32px; }
  .venue {
    position: absolute;
    top: 1090px;
    left: 0; right: 0;
    font-size: 23px;
    font-weight: 600;
  }
  .web-band {
    position: absolute;
    left: 0; right: 0; bottom: 0;
    height: 62px;
    background: var(--band);
    color: var(--white);
    font-size: 27px;
    font-weight: 800;
    font-style: italic;
    letter-spacing: 3px;
    display: flex;
    align-items: center;
    justify-content: center;
  }
</style>
</head>
<body>
  <main class="poster">
    <div class="scenery" role="img" aria-label="Photo of a tropical lake with a waterfall, green forest and blue sky"></div>
    <div class="notes-art" role="img" aria-label="Illustration of musical notes rising from a burst of light"></div>

    <h2 class="tagline">Chanting,<br>Dancing &amp; Feasting</h2>

    <h1 class="event-name">Velvet<br>Ember</h1>
    <p class="event-type">MUSIC EVENT</p>
    <p class="admission">- NO CHARGE -</p>

    <p class="invitation">
      You are warmly invited to join us<br>
      for an evening of live music,<br>
      mantra meditation &amp; free vegetarian dinner!
    </p>

    <p class="schedule">
      <span>Every Sunday at</span>
      <svg viewBox="0 0 30 30" aria-hidden="true">
        <circle cx="15" cy="15" r="12" fill="none" stroke="#1b2a6b" stroke-width="3"/>
        <path d="M15 8 V15 L20 18" fill="none" stroke="#1b2a6b" stroke-width="3" stroke-linecap="round"/>
      </svg>
      <span class="time">6:00 PM</span>
    </p>

    <p class="venue">412 Maneola Rd. Pahoa Hi &nbsp;·&nbsp; Ph: 808.555.0193</p>

    <footer class="web-band">WWW.ISLANDCHANTGATHERING.COM</footer>
  </main>
</body>
</html>
```